R.K Landscaping 484-883-7758Mulching Mowing Planting Spring and Fall Clean up

The colors I would like to work with Are black and green.I do have a Facebook page it's https://www.vernetsocial.example/RK-Landscaping-902145638870214/

For my business logo I would like to put that either on the corner or in the background

Services: mowing, mulching, fall and spring cleanup, hedge trimming

Requirements
Must have
• Please use these pics
• I like Design #9926064
• and room for addresses to
Should not have
• the pics in the back of card

```html
<!DOCTYPE html>
<html lang="en">
<head>
<meta charset="utf-8">
<title>R.K Landscaping – Postcard</title>
<link rel="stylesheet" href="https://fonts.googleapis.com/css2?family=Oswald:wght@400;500&family=Montserrat:wght@400;500;600&family=Lora:ital,wght@1,700&display=swap">
<style>
  :root {
    --page: #e9e6e1;
    --green: #2b9b48;
    --green-deep: #167c3e;
    --green-dark: #0f5a2a;
    --black: #0d0d0d;
    --white: #ffffff;
    --cream: #fbf3c2;
    --grey: #f0f1f3;
    --text: #1b1b1b;
  }
  * { box-sizing: border-box; margin: 0; padding: 0; }
  html, body { width: 1200px; height: 1000px; overflow: hidden; }
  body { background: var(--page); position: relative; font-family: "Montserrat", sans-serif; }

  .card { position: absolute; width: 610px; height: 473px; overflow: hidden; box-shadow: 0 4px 14px rgba(0,0,0,.25); }
  .card--front { left: 40px; top: 18px; background: var(--white); }
  .card--back { left: 528px; top: 503px; background: var(--grey); }

  .photo { position: absolute; }
  .front-photo { left: 0; top: 0; width: 610px; height: 320px;
    background: linear-gradient(180deg, #8fb4d6 0%, #5f7f4a 22%, #4f7335 45%, #5f8f3a 70%, #4d7a2e 100%); }
  .back-photo { left: 0; top: 0; width: 456px; height: 153px;
    background: linear-gradient(180deg, #6e8a5c 0%, #3f5e2c 40%, #5f9a3c 75%, #6aa541 100%); }

  .front-wave { position: absolute; left: 0; top: 250px; width: 610px; height: 90px; }

  .brand { position: absolute; display: flex; flex-direction: column; align-items: center; }
  .brand-row { display: flex; align-items: center; gap: 8px; }
  .brand-mark { width: 16px; height: 16px; background: var(--black); border-radius: 50%; }
  .brand-name { font-family: "Oswald", sans-serif; font-weight: 500; color: var(--black); letter-spacing: .5px; text-transform: uppercase; white-space: nowrap; }
  .card--front .brand { left: 40px; top: 150px; }
  .card--front .brand-name { font-size: 30px; }
  .brand-tagline { font-family: "Lora", serif; font-style: italic; font-weight: 700; font-size: 12px; line-height: 14px; color: var(--black); text-align: center; margin-top: 4px; }
  .card--back .brand { left: 30px; top: 108px; }
  .card--back .brand-name { font-size: 22px; }

  .call-box { position: absolute; left: 0; top: 297px; width: 262px; height: 108px; background: var(--green); border-radius: 0 10px 0 0; }
  .call-box::after { content: ""; position: absolute; left: 0; bottom: -4px; width: 262px; height: 4px; background: #555; }
  .call-label { position: absolute; left: 40px; top: 4px; font-family: "Oswald", sans-serif; font-size: 33px; color: var(--white); white-space: nowrap; }
  .call-strip { position: absolute; left: 6px; top: 50px; width: 250px; height: 2px; background: var(--white); }
  .call-number { position: absolute; left: 0; top: 52px; width: 262px; text-align: center; font-family: "Oswald", sans-serif; font-size: 40px; line-height: 50px; color: var(--cream); white-space: nowrap; }

  .services { position: absolute; }
  .services-title { font-weight: 600; text-transform: uppercase; }
  .services-list { list-style: none; }
  .service { display: inline-flex; align-items: center; gap: 3px; white-space: nowrap; }
  .tick { width: 11px; height: 11px; flex: none; }
  .card--front .services { left: 302px; top: 317px; }
  .card--front .services-title { color: var(--green); font-size: 17px; }
  .card--front .services-list { font-size: 16.5px; color: var(--text); line-height: 23px; }
  .card--front .service--pair { margin-left: 24px; }

  .follow-bar { position: absolute; left: 0; top: 420px; width: 610px; height: 53px; background: var(--black);
    display: flex; align-items: center; justify-content: center; gap: 10px; font-size: 17px; }
  .follow-label { color: var(--green); }
  .social-square { width: 30px; height: 30px; background: var(--cream); border-radius: 4px; }
  .social-name { color: var(--white); }

  .back-panel { position: absolute; left: 0; top: 153px; width: 292px; height: 236px; background: var(--green-deep); color: var(--white); }
  .back-strip { position: absolute; left: 0; top: 389px; width: 75px; height: 84px; background: var(--green-deep); }
  .card--back .services { left: 0; top: 16px; width: 292px; text-align: center; }
  .card--back .services-title { color: var(--cream); font-size: 15px; }
  .card--back .services-list { font-size: 14.5px; line-height: 21px; margin-top: 3px; }
  .card--back .service--pair { margin-left: 16px; }
  .divider { position: absolute; left: 42px; top: 108px; width: 204px; border-top: 2px dotted rgba(255,255,255,.7); }
  .back-call { position: absolute; left: 0; top: 118px; width: 292px; text-align: center; }
  .back-call-label { font-family: "Oswald", sans-serif; font-size: 22px; }
  .back-call-number { font-size: 28px; color: var(--cream); margin-top: 2px; white-space: nowrap; }
  .back-follow { margin-top: 6px; display: flex; align-items: center; justify-content: center; gap: 7px; font-size: 13px; font-weight: 500; white-space: nowrap; }
  .back-follow .social-square { width: 22px; height: 22px; }
</style>
</head>
<body>

<section class="card card--front">
  <div class="photo front-photo" role="img" aria-label="Photo of a freshly mowed lawn behind a two-storey house with a wooden deck"></div>
  <svg class="front-wave" viewBox="0 0 610 90" preserveAspectRatio="none" aria-hidden="true">
    <path d="M0 48 C120 20 260 10 380 30 C480 46 560 64 610 56 L610 90 L0 90 Z" fill="var(--green-dark)"/>
    <path d="M0 56 C120 32 260 24 380 42 C480 58 560 76 610 70 L610 90 L0 90 Z" fill="var(--white)"/>
  </svg>

  <div class="brand">
    <div class="brand-row"><span class="brand-mark"></span><span class="brand-name">R.K Landscaping</span></div>
    <p class="brand-tagline">For all your Professional<br>Landscaping Needs</p>
  </div>

  <div class="call-box">
    <p class="call-label">Call Us Today at</p>
    <div class="call-strip"></div>
    <p class="call-number">312-555-0194</p>
  </div>

  <div class="services">
    <p class="services-title">Services Offered</p>
    <ul class="services-list">
      <li><span class="service"><svg class="tick" viewBox="0 0 11 11"><rect x=".5" y=".5" width="10" height="10" fill="none" stroke="var(--green)"/><path d="M2.5 5.5 L4.5 7.5 L8.5 2.5" fill="none" stroke="var(--green)" stroke-width="1.4"/></svg>Mowing</span><span class="service service--pair"><svg class="tick" viewBox="0 0 11 11"><rect x=".5" y=".5" width="10" height="10" fill="none" stroke="var(--green)"/><path d="M2.5 5.5 L4.5 7.5 L8.5 2.5" fill="none" stroke="var(--green)" stroke-width="1.4"/></svg>Mulching</span></li>
      <li><span class="service"><svg class="tick" viewBox="0 0 11 11"><rect x=".5" y=".5" width="10" height="10" fill="none" stroke="var(--green)"/><path d="M2.5 5.5 L4.5 7.5 L8.5 2.5" fill="none" stroke="var(--green)" stroke-width="1.4"/></svg>Fall and Spring Cleanup</span></li>
      <li><span class="service"><svg class="tick" viewBox="0 0 11 11"><rect x=".5" y=".5" width="10" height="10" fill="none" stroke="var(--green)"/><path d="M2.5 5.5 L4.5 7.5 L8.5 2.5" fill="none" stroke="var(--green)" stroke-width="1.4"/></svg>Hedge Trimming</span></li>
    </ul>
  </div>

  <div class="follow-bar">
    <span class="follow-label">Follow us at</span>
    <span class="social-square"></span>
    <span class="social-name">RK-Landscaping</span>
  </div>
</section>

<section class="card card--back">
  <div class="photo back-photo" role="img" aria-label="Photo of a green front lawn with shrubs and a porch"></div>
  <div class="brand">
    <div class="brand-row"><span class="brand-mark"></span><span class="brand-name">R.K Landscaping</span></div>
  </div>

  <div class="back-panel">
    <div class="services">
      <p class="services-title">Services Offered</p>
      <ul class="services-list">
        <li><span class="service"><svg class="tick" viewBox="0 0 11 11"><path d="M1.5 5.5 L4.5 8.5 L9.5 1.5" fill="none" stroke="var(--white)" stroke-width="1.6"/></svg>Mowing</span><span class="service service--pair"><svg class="tick" viewBox="0 0 11 11"><path d="M1.5 5.5 L4.5 8.5 L9.5 1.5" fill="none" stroke="var(--white)" stroke-width="1.6"/></svg>Mulching</span></li>
        <li><span class="service"><svg class="tick" viewBox="0 0 11 11"><path d="M1.5 5.5 L4.5 8.5 L9.5 1.5" fill="none" stroke="var(--white)" stroke-width="1.6"/></svg>Fall and Spring Cleanup</span></li>
        <li><span class="service"><svg class="tick" viewBox="0 0 11 11"><path d="M1.5 5.5 L4.5 8.5 L9.5 1.5" fill="none" stroke="var(--white)" stroke-width="1.6"/></svg>Hedge Trimming</span></li>
      </ul>
    </div>
    <div class="divider"></div>
    <div class="back-call">
      <p class="back-call-label">Call Us Today at</p>
      <p class="back-call-number">312-555-0194</p>
      <p class="back-follow">Follow us at <span class="social-square"></span> RK-Landscaping</p>
    </div>
  </div>
  <div class="back-strip"></div>
</section>

</body>
</html>
```